Home page concept, possible logo colour change

There is no need to code a home page, we are just looking for concept ideas.
We have had a logo designed for a new company we are starting named Corvenhall Aluminium Windows & Doors. We are manufacturing bullet resistant window frames. We have had logo designed, we like the concept of the design, but the current colours (black and red) may not be the best option, especially when designing the website home page, and how it interacts with the logo colours. I have also attached the first draft of the home page which we are not happy with. The overall design/navigation is good, we have issues with the darkened out primary image and also the amount of red on the page, it just doesn't feel right. As mentioned before we are happy to look at colour changes to the logo.
Number of Pages Required
1 page
Look and feel
Each slider illustrates characteristics of the customer's brand and the style your logo design should communicate.

```html
<!DOCTYPE html>
<html lang="en">
<head>
<meta charset="utf-8">
<title>Corvenhall Aluminium Windows &amp; Doors</title>
<link href="https://fonts.googleapis.com/css2?family=Poppins:wght@400;500;600;700&display=swap" rel="stylesheet">
<style>
:root{
  --olive:#828b15;
  --olive-dark:#5f6610;
  --ink:#1b1b1b;
  --text:#3a3a3a;
  --cream:#f5f5ea;
  --mist:#f2f4f8;
  --white:#ffffff;
}
*{margin:0;padding:0;box-sizing:border-box}
html,body{width:1200px;height:3291px;overflow:hidden}
body{font-family:'Poppins',sans-serif;color:var(--text);background:var(--white);position:relative}
a{text-decoration:none;color:inherit}

/* hero */
.hero{position:absolute;top:0;left:0;width:1200px;height:740px;background:linear-gradient(180deg,#eef0f4 0%,#ffffff 60%,#e9ecf2 100%)}
.brand{position:absolute;left:85px;top:58px;display:flex;align-items:center;gap:12px}
.brand-name{font-size:34px;font-weight:600;color:var(--olive);line-height:1}
.brand-sub{font-size:9.5px;font-weight:600;letter-spacing:1.4px;color:#444;text-transform:uppercase;margin-top:4px}
.brand-dot{width:16px;height:16px;border-radius:50%;background:var(--olive)}
.nav{position:absolute;top:60px;right:85px;display:flex;align-items:center;gap:42px;font-size:15px;color:#333}
.nav .active{color:var(--olive);padding-bottom:12px;border-bottom:3px solid var(--olive);margin-top:14px}
.nav .btn{background:var(--olive);color:#fff;padding:13px 19px;border-radius:3px;font-size:14px}
.hero-photo{position:absolute;left:180px;top:185px;width:235px;height:535px;background:linear-gradient(100deg,#8d95a6,#b9d0d8 30%,#cfdfe4 70%,#848a98);border-radius:2px}
.hero-copy{position:absolute;left:515px;top:268px;width:510px}
.hero-copy h1{font-size:57px;font-weight:700;color:var(--olive);line-height:61px}
.hero-copy h2{font-size:31px;font-weight:600;color:#111;margin-top:14px}
.hero-copy p{font-size:15px;line-height:26px;margin-top:14px;color:#444}
.outline-btn{display:inline-block;border:2px solid var(--olive);color:var(--olive);font-size:13px;padding:14px 36px;margin-top:38px;text-transform:uppercase}

/* features */
.features{position:absolute;top:740px;left:0;width:1200px;height:425px;background:#fff}
.feature{position:absolute;top:120px;width:338px;height:238px;border-radius:22px;text-align:center;padding-top:118px}
.feature.cream{background:var(--cream)}
.feature.mist{background:var(--mist)}
.feature .ring{position:absolute;left:50%;top:-64px;width:138px;height:138px;margin-left:-69px;border-radius:50%;border:3px solid var(--olive);background:#fff;display:flex;align-items:center;justify-content:center}
.feature .ring.filled{background:var(--olive);border-color:var(--olive)}
.feature h3{font-size:24px;font-weight:600;color:var(--olive)}
.feature p{font-size:15px;color:#222;line-height:24px;margin-top:8px}

/* products */
.products{position:absolute;top:1165px;left:0;width:1200px;height:753px;background:var(--cream)}
.products h2{position:absolute;top:106px;width:100%;text-align:center;font-size:32px;font-weight:600;color:var(--olive)}
.card{position:absolute;top:200px;width:325px;height:450px;background:#fff;border-radius:6px;text-align:center;padding:8px}
.card .photo{height:230px;border-radius:3px}
.card h3{font-size:26px;font-weight:500;color:var(--olive);margin-top:30px}
.card p{font-size:15px;line-height:24px;color:#333;text-align:justify;text-align-last:center;padding:0 19px;margin-top:14px}
.card .cta{position:absolute;left:50%;bottom:-16px;transform:translateX(-50%);border:1px solid var(--olive);color:var(--olive);background:#fff;font-size:13px;padding:7px 17px;white-space:nowrap}
.card .cta.solid{background:var(--olive);color:#fff}

/* highlights */
.highlights{position:absolute;top:1918px;left:0;width:1200px;height:332px;background:#fff}
.bullets{position:absolute;top:96px;left:265px;display:flex;gap:46px}
.bullet{display:flex;gap:16px;font-size:30px;font-weight:600;color:#111;line-height:30px}
.bullet::before{content:"";width:11px;height:11px;border-radius:50%;background:var(--olive);margin-top:10px;flex:none}
.big-btn{position:absolute;top:206px;left:466px;width:268px;height:64px;background:var(--olive);color:#fff;font-size:28px;font-weight:600;display:flex;align-items:center;justify-content:center}

/* process */
.process{position:absolute;top:2250px;left:0;width:1200px;height:633px;background:var(--cream)}
.acc{position:absolute;left:86px;width:518px}
.acc-item{border-bottom:2px solid #dcdcd0;padding:0 16px}
.acc-head{display:flex;align-items:center;font-size:21px;font-weight:500;color:#222;height:88px}
.acc-head .num{color:var(--olive);font-weight:600;margin-right:14px}
.acc-head .sign{margin-left:auto;color:var(--olive);font-size:28px;font-weight:400}
.acc-body{font-size:15px;line-height:25px;color:#333;text-align:justify;margin-top:-6px}
.acc-link{display:block;color:var(--olive);font-size:18px;margin:24px 0 30px}
.process-photo{position:absolute;left:714px;top:62px;width:401px;height:491px;background:radial-gradient(circle at 50% 50%,#bfc2c4 0 35%,#1d1d1f 36% 60%,#f7f7f7 61%)}

/* footer */
.footer{position:absolute;top:2883px;left:0;width:1200px;height:350px;background:var(--olive);color:#fff}
.footer .brand{left:85px;top:130px}
.footer .brand-name{color:#fff}
.footer .brand-sub{color:#fff}
.footer .brand-dot{background:#fff}
.fcol{position:absolute;top:98px}
.fcol h4{font-size:14px;font-weight:600;text-transform:uppercase}
.fcol ul{list-style:none;margin-top:28px;font-size:15px;line-height:26px}
.fcol li::before{content:"\2726";font-size:10px;margin-right:6px}
.contact{margin-top:32px;font-size:15px;line-height:18px}
.contact .row{display:flex;gap:12px;margin-bottom:16px}
.contact .ico{width:22px;height:22px;border-radius:4px;background:#fff;flex:none;display:flex;align-items:center;justify-content:center}
.badge{margin-top:30px;margin-left:38px;width:90px;height:58px;background:#fff;border-radius:2px;display:flex;align-items:center;justify-content:center}
.copyright{position:absolute;top:3233px;left:0;width:1200px;height:58px;background:var(--olive-dark);color:#fff;font-size:15px;display:flex;align-items:center;justify-content:center}
</style>
</head>
<body>

<section class="hero">
  <div class="brand">
    <div>
      <div class="brand-name">Corvenhall</div>
      <div class="brand-sub">Aluminium Windows &amp; Doors</div>
    </div>
    <span class="brand-dot"></span>
  </div>
  <nav class="nav">
    <a class="active" href="#">Home</a>
    <a href="#">Our Products &#9662;</a>
    <a href="#">Why Corvenhall</a>
    <a class="btn" href="#">Make an Enquiry</a>
  </nav>
  <div class="hero-photo" role="img" aria-label="Grey aluminium framed bullet resistant door with frosted glass"></div>
  <div class="hero-copy">
    <h1>Bullet Resistant Window &amp; Doors</h1>
    <h2>Your First Line of Defence</h2>
    <p>Lorem ipsum dolor sit amet, consectetur adipiscing elit, sed do eiusmod tempor incididunt ut labore et dolore magna aliqua. Ut enim ad minim veniam, quis nostrud exercitation ullamco laboris nisi ut aliquip ex ea commodo consequat.</p>
    <a class="outline-btn" href="#">Know More</a>
  </div>
</section>

<section class="features">
  <div class="feature cream" style="left:86px">
    <div class="ring">
      <svg width="58" height="66" viewBox="0 0 58 66"><path d="M29 2 L54 12 V32 C54 48 43 59 29 64 C15 59 4 48 4 32 V12 Z" fill="#828b15"/><path d="M17 33 L26 42 L42 24" stroke="#fff" stroke-width="6" fill="none" stroke-linecap="round" stroke-linejoin="round"/></svg>
    </div>
    <h3>Premium Protection</h3>
    <p>Lorem ipsum dolor sit amet,<br>consectetur adipiscing elit</p>
  </div>
  <div class="feature mist" style="left:432px">
    <div class="ring filled">
      <svg width="70" height="70" viewBox="0 0 70 70" fill="#fff"><rect x="2" y="4" width="28" height="14"/><rect x="40" y="4" width="28" height="14"/><rect x="2" y="28" width="66" height="14"/><rect x="2" y="52" width="28" height="14"/><rect x="40" y="52" width="28" height="14"/></svg>
    </div>
    <h3>Aesthetically Designed</h3>
    <p>Lorem ipsum dolor sit amet,<br>consectetur adipiscing elit</p>
  </div>
  <div class="feature cream" style="left:779px">
    <div class="ring">
      <svg width="70" height="56" viewBox="0 0 70 56" fill="none" stroke="#828b15" stroke-width="4"><circle cx="16" cy="16" r="12"/><path d="M16 9 V16 H22"/><path d="M30 16 H46 V42 H10 V30"/><path d="M46 24 H58 L66 34 V42 H46"/><circle cx="20" cy="46" r="6" fill="#fff"/><circle cx="56" cy="46" r="6" fill="#fff"/></svg>
    </div>
    <h3>Promptly Delivered</h3>
    <p>Lorem ipsum dolor sit amet,<br>consectetur adipiscing elit</p>
  </div>
</section>

<section class="products">
  <h2>Superior Protection, Sleek Design</h2>
  <div class="card" style="left:82px">
    <div class="photo" role="img" aria-label="Grey aluminium door with frosted glass panel" style="background:linear-gradient(90deg,#f1f2f6,#9aa1b0 30%,#c3d8dd 45%,#c7dade 60%,#8e95a4 66%,#e4e6ee)"></div>
    <h3>Product</h3>
    <p>Lorem ipsum dolor sit amet, conectetur adipiscing elit, sed do eiusmod tempor incididunt ut</p>
    <a class="cta" href="#">Learn More</a>
  </div>
  <div class="card" style="left:437px">
    <div class="photo" role="img" aria-label="Black framed aluminium door standing open" style="background:linear-gradient(90deg,#f1f2f6,#1d1d1f 30%,#c3d8dd 40%,#c7dade 66%,#1d1d1f 72%,#e4e6ee)"></div>
    <h3>Product</h3>
    <p>Lorem ipsum dolor sit amet, conectetur adipiscing elit, sed do eiusmod tempor incididunt ut</p>
    <a class="cta solid" href="#">Learn More</a>
  </div>
  <div class="card" style="left:792px">
    <div class="photo" role="img" aria-label="Building facade with window frames reflecting cloudy sky" style="background:linear-gradient(110deg,#46556a 0 25%,#8fb0d6 30%,#e6edf4 55%,#7ea4d0 80%,#4f6c92)"></div>
    <h3>Enquire</h3>
    <p>Lorem ipsum dolor sit amet, conectetur adipiscing elit, sed do eiusmod tempor incididunt ut</p>
    <a class="cta" href="#">Enquire now</a>
  </div>
</section>

<section class="highlights">
  <div class="bullets">
    <div class="bullet">Premium<br>Protection</div>
    <div class="bullet" style="margin-left:2px">Aesthetically<br>Designed</div>
    <div class="bullet" style="margin-left:24px">Promptly<br>Delivered</div>
  </div>
  <a class="big-btn" href="#">Make an Enquiry</a>
</section>

<section class="process">
  <div class="acc" style="top:12px">
    <div class="acc-item">
      <div class="acc-head"><span class="num">01</span>Explore Our Range<span class="sign">&minus;</span></div>
      <p class="acc-body">Lorem ipsum dolor sit amet, consectetur adipiscing elit, sed do eiusmod tempor incididunt ut labore et dolore magna aliqua. Ut enim ad minim veniam, quis nostrud exercitation ullamco laboris nisi ut aliquip ex ea commoo consequat. Duis aute irure dolor in reprehenderit</p>
      <a class="acc-link" href="#">Make An Enquiry</a>
    </div>
    <div class="acc-item">
      <div class="acc-head"><span class="num">02</span>Make An Enquiry<span class="sign">+</span></div>
    </div>
    <div class="acc-item">
      <div class="acc-head"><span class="num">03</span>Receive Customised Quote<span class="sign">+</span></div>
    </div>
  </div>
  <div class="process-photo" role="img" aria-label="Black aluminium window frame with frosted glass, angled view"></div>
</section>

<footer class="footer">
  <div class="brand">
    <div>
      <div class="brand-name">Corvenhall</div>
      <div class="brand-sub">Aluminium Windows &amp; Doors</div>
    </div>
    <span class="brand-dot"></span>
  </div>
  <div class="fcol" style="left:389px;top:100px">
    <h4>Quick Links</h4>
    <ul><li>Home</li><li>Why Corvenhall</li><li>Make an Enquiry</li><li>Our Products</li><li>Blog</li></ul>
  </div>
  <div class="fcol" style="left:615px">
    <h4>Contact Us</h4>
    <div class="contact">
      <div class="row"><span class="ico"><svg width="12" height="14" viewBox="0 0 12 14"><path d="M6 0 C2.7 0 0 2.6 0 5.8 C0 9.8 6 14 6 14 S12 9.8 12 5.8 C12 2.6 9.3 0 6 0Z" fill="#828b15"/><circle cx="6" cy="5.8" r="2.2" fill="#fff"/></svg></span><div><strong>Sydney</strong><br>24 Harrow Lane<br>Ashford, NSW 2010 AU</div></div>
      <div class="row"><span class="ico"><svg width="12" height="12" viewBox="0 0 12 12"><path d="M2 1 L4.5 1 L5.5 4 L4 5 C4.8 6.8 5.2 7.2 7 8 L8 6.5 L11 7.5 V10 C11 10.6 10.5 11 10 11 C5 11 1 7 1 2 C1 1.5 1.4 1 2 1Z" fill="#828b15"/></svg></span>+61 2 5550 1847</div>
      <div class="row"><span class="ico"><svg width="12" height="10" viewBox="0 0 12 10"><rect x="0" y="0" width="12" height="10" rx="1" fill="#828b15"/><path d="M0.5 1 L6 5.5 L11.5 1" stroke="#fff" fill="none"/></svg></span>info@corvenhall.com</div>
    </div>
  </div>
  <div class="fcol" style="left:865px">
    <h4>Quality Assurance</h4>
    <div class="badge"><span style="width:36px;height:30px;background:var(--olive);border-radius:3px;display:block"></span></div>
  </div>
</footer>
<div class="copyright">Copyright &copy; 2023 All Rights Reserved By Corvenhall</div>

</body>
</html>
```